Modern Website Design for an Online Travel Agency.. Design Only!!

Hi there!

We are building an website for our travel agency that caters to tourists traveling to the Cayman Islands. We provide travel information and take bookings for various tours available here.

We need designs for 8 different web page layouts. You can see the layout specifications in two attached documents. We do not have a need for the coding to be done. This will simply act as a blueprint for our developer to build from.

The important pages are the 'Home Page' 'checkout page' and the ‘Checkout Page’ (Page 1 & 10 in the PDF ‘Website Layout’)

The MOST important page is ‘Tour Search Page’ (page 6)

If you intend on only submitting one page design, please submit a design for page 6. Be aware though, the more of these 3 page designs you submit, the more likely we are to move forward with you!

At this stage, we are simply looking to develop the most aesthetic website design layout possible.

- The website should be colour coordinated with the logo. You can most certainly use other colours if you feel they complement the overall design of the website well.

- Everything must be laid out in an EXTREMELY simple & ‘easy to navigate’ way. The key is simplicity & Functionality. There is no need for messy or elaborate graphics.

- The website MUST have a VERY clean and modern appearance.

- We want the main background to be white, but you can use light grey in places to compliment or add dimension if you feel necessary.

- We will appreciate a good use of shadows and especially a good use of icons. (You can see examples of icons we have already designed, we are definitely open to new icon design concepts too)

- We will reward imagination and original thinking! Essentially we want a website with a creative touch and unique design elements, whilst maintaining that clean and simple layout.

- Most importantly!! - Paying attention to the small details will be highly rewarded (A well balanced and seamless use of fonts, colours, dimensions, shadowing, positioning, etc)

If you have any questions, please don’t hesitate to ask.

We’re excited to see your design submissions!

Thank you!!

You can find all the support documents and content at: https://www.filvanta.net/sh/8qm3tzprwevan47/BBQWmTfPnRxLoXEwuuiYcPvQb?dl=0

Target Market(s)

Tourists

Industry/Entity Type

Travel

Number of Pages Required

5+ page

Font styles to use
Sans Serif

Colors

Designer to choose colors to be used in the design.

Requirements
Must have
• Must be very clean and modern.
• Must be simple and bold
• Must be color coordinated in a way that makes sense
• White background
Nice to have
• Good use of shadows and Icons
Should not have
• Over use of messy graphics
• And design layout which is not right angled (using anything but vertical or horizontal for the edges in the design)

```html
<!DOCTYPE html>
<html lang="en">
<head>
<meta charset="utf-8">
<title>TideRoute – Horse Ride along the Beach</title>
<link href="https://fonts.googleapis.com/css2?family=Poppins:wght@300;400;500;600&display=swap" rel="stylesheet">
<style>
:root{
  --green:#6aac1f;
  --green-dark:#4f8a12;
  --blue:#2a7fd4;
  --ink:#1b1b1b;
  --text:#333;
  --muted:#777;
  --grey:#f1f1f1;
  --grey-2:#e4e4e4;
  --grey-3:#dadada;
  --black:#111;
  --white:#fff;
}
*{box-sizing:border-box;margin:0;padding:0}
html,body{width:1200px;height:5205px;overflow:hidden}
body{position:relative;background:var(--white);font-family:"Poppins",sans-serif;color:var(--text)}
.abs{position:absolute}
a{color:inherit;text-decoration:none}
.read-more{color:var(--green);font-size:14px;font-weight:500}
.read-more::after{content:" »"}
.fill{position:absolute}

/* hero */
.hero{left:0;top:0;width:1200px;height:562px;background:linear-gradient(180deg,#1f2326 0%,#2d3235 45%,#3b3f3f 70%,#1a1c1d 100%)}
.brand{display:flex;align-items:center;gap:10px;font-weight:500;color:var(--green)}
.brand .mark{background:var(--green);display:block}
.hero .brand{left:117px;top:50px;font-size:32px}
.hero .brand .mark{width:34px;height:34px}
.topbar{top:30px;font-size:12px;color:var(--white)}
.mainnav{top:67px;font-size:13px;color:var(--white)}
.mainnav .active,.topbar .active{color:var(--green)}
.hero-title{left:0;width:1200px;top:218px;text-align:center;color:var(--white);font-size:52px;font-weight:400;line-height:64px;letter-spacing:1px}
.hero-title span{color:var(--green);font-weight:600;text-decoration:underline;text-decoration-thickness:3px;text-underline-offset:4px}

/* intro cards */
.card{background:var(--white);top:513px;height:457px;width:477px;box-shadow:0 4px 18px rgba(0,0,0,.08)}
.card h2{font-size:40px;font-weight:500;color:var(--ink);line-height:46px}
.about{left:115px;padding:24px 30px}
.about ul{list-style:none;margin-top:56px}
.about li{position:relative;padding-left:26px;font-size:20px;line-height:26px;color:var(--ink);margin-bottom:13px}
.about li::before{content:"";position:absolute;left:0;top:9px;width:10px;height:10px;border-radius:50%;background:var(--green)}
.company{left:606px;padding:24px 36px}
.company p{font-size:13px;line-height:26px;margin-top:20px;color:var(--text)}
.company .read-more{display:block;margin-top:8px}
.organized{font-size:11px;color:var(--muted);margin-top:18px}
.badge{width:84px;height:64px;background:#5a2a1c;margin-top:8px}
.describes{display:block;font-size:11px;color:var(--muted);text-decoration:underline;margin-top:6px}

/* activity */
.activity-title{left:117px;top:1124px;font-size:40px;font-weight:500;color:var(--ink)}
.activity-text{left:117px;top:1188px;width:470px;font-size:13px;line-height:26px}
.activity .read-more{left:117px;top:1320px}
.chip{top:1390px;width:150px;height:58px;background:var(--green);color:var(--white);font-size:13px;line-height:17px;display:flex;align-items:center;padding-left:44px;padding-right:24px}
.chip::after{content:"";position:absolute;right:0;top:0;width:20px;height:58px;background:var(--green-dark)}
.chip svg{position:absolute;right:5px;top:22px;z-index:1}
.chip .ico{position:absolute;left:12px;top:19px;width:22px;height:20px;border:2px solid rgba(255,255,255,.5);border-radius:3px}

/* booking band */
.band{left:0;top:1612px;width:1200px;height:540px;background:linear-gradient(180deg,#3f78b7 0%,#6e9fd0 30%,#a7c0cf 55%,#d7d1c4 75%,#e6e1d6 100%)}
.price-card{left:612px;top:1612px;width:471px;height:540px}
.price-top{height:128px;background:var(--black);color:var(--white);text-align:center;padding-top:26px}
.price-top small{display:block;font-size:22px;font-weight:300}
.price-top strong{display:block;font-size:42px;font-weight:500;line-height:52px}
.price-mid{height:323px;background:var(--grey);text-align:center;padding-top:68px}
.reviews{display:block;font-size:17px;text-decoration:underline;color:var(--text);margin-top:6px}
.btn-book{display:block;width:289px;height:81px;margin:24px auto 0;background:var(--green);color:var(--white);font-size:34px;font-weight:500;line-height:81px}
.contact-row{display:flex;height:89px}
.contact-row a{flex:1;background:var(--grey-2);display:flex;align-items:center;justify-content:center;gap:8px;font-size:19px;color:#555}
.contact-row a+a{margin-left:4px}

/* tours */
.section-title{left:0;width:1200px;text-align:center;font-size:44px;font-weight:500;color:var(--ink)}
.tour{left:115px;width:968px;height:147px;background:var(--grey)}
.tour .icon-box{position:absolute;left:0;top:0;width:128px;height:147px;background:var(--grey-2);display:flex;align-items:center;justify-content:center}
.tour h3{position:absolute;left:142px;top:56px;font-size:28px;font-weight:500;color:var(--ink)}
.tour .price{position:absolute;left:368px;top:62px;font-size:20px;font-weight:500;color:var(--ink)}
.tour .price b{color:var(--green);font-weight:500}
.tour .btn{position:absolute;top:46px;height:57px;font-size:13px;display:flex;align-items:center;padding-left:38px}
.tour .btn::after{content:"";position:absolute;right:0;top:0;width:22px;height:57px;background:var(--green-dark)}
.tour .btn svg{position:absolute;right:6px;top:22px;z-index:1}
.tour .btn-primary{left:596px;width:168px;background:var(--green);color:var(--white)}
.tour .btn-outline{left:776px;width:170px;background:var(--white);border:1px solid var(--grey-3);padding-left:16px;color:#444}
.tour-more{right:121px}

/* meeting */
.map{left:0;top:2859px;width:600px;height:311px;background:linear-gradient(135deg,#cfe4fb 0%,#dfecf6 40%,#eef1f3 60%,#e7ebee 100%)}
.meeting-bg{left:600px;top:2859px;width:600px;height:311px;background:var(--grey)}
.meeting-title{left:636px;top:2928px;font-size:40px;font-weight:500;color:var(--ink)}
.meeting-addr{left:636px;top:3010px;width:420px;font-size:13px;line-height:24px;color:var(--ink)}
.meeting .read-more{left:636px;top:3078px}

/* gallery */
.photo{position:absolute}

/* steps */
.step-art{position:absolute;width:210px;height:200px;background:linear-gradient(160deg,#eaf4fb 0%,#dcefd0 100%)}
.step-num{position:absolute;width:36px;height:36px;border-radius:50%;background:#dcecfb;color:var(--blue);font-size:18px;text-align:center;line-height:36px}
.step-title{position:absolute;width:240px;font-size:21px;font-weight:500;line-height:29px;color:var(--ink)}
.step-title.blue{color:var(--blue)}
.recommended{left:655px;top:4061px;width:545px;height:808px;background:linear-gradient(180deg,#0c0c0c 0%,#1a1208 45%,#6b4210 68%,#2a1a08 85%,#0d0a06 100%)}
.recommended h2{position:absolute;left:46px;top:56px;font-size:40px;font-weight:500;line-height:48px;color:var(--white)}

/* footer */
.footer{left:0;top:4869px;width:1200px;height:273px;background:var(--grey)}
.footer .brand{position:absolute;left:0;width:1200px;justify-content:center;top:100px;font-size:52px}
.footer .brand .mark{width:50px;height:50px}
.footnav{position:absolute;top:200px;left:0;width:1200px;display:flex;justify-content:center;gap:46px;font-size:14px;color:var(--ink)}
.footnav .active{color:var(--green)}
.copyright{left:0;top:5142px;width:1200px;height:63px;background:var(--grey-3);text-align:center;line-height:63px;font-size:12px;color:#444}
</style>
</head>
<body>

<!-- Hero -->
<header>
  <div class="abs hero" role="img" aria-label="Photo of two riders on horseback at the beach under a moonlit night sky"></div>
  <a class="abs brand" href="#"><span class="mark"></span>TideRoute</a>
  <nav class="abs topbar" style="left:868px"><a class="active" href="#">Destination</a></nav>
  <nav class="abs topbar" style="left:982px"><a href="#">USD$</a></nav>
  <nav class="abs topbar" style="left:1026px;display:flex;align-items:center;gap:3px">
    <svg width="14" height="14" viewBox="0 0 14 14" fill="none" stroke="#fff" stroke-width="1.2"><circle cx="7" cy="7" r="6"/><circle cx="7" cy="5.5" r="2"/><path d="M3.3 11.2c1-1.6 2.2-2.2 3.7-2.2s2.7.6 3.7 2.2"/></svg>
    <a href="#">LOGIN</a>
  </nav>
  <nav class="abs mainnav" style="left:535px"><a class="active" href="#">Discover Cayman</a></nav>
  <nav class="abs mainnav" style="left:689px"><a href="#">Things To do</a></nav>
  <nav class="abs mainnav" style="left:808px"><a href="#">My Trip Planner</a></nav>
  <nav class="abs mainnav" style="left:945px"><a href="#">Map</a></nav>
  <nav class="abs mainnav" style="left:1010px"><a href="#">Contact Us</a></nav>
  <h1 class="abs hero-title">Horse Ride along the Beach<br>in <span>Grand Cayman</span></h1>
</header>

<!-- Intro cards -->
<section class="abs card about">
  <h2>About the Tour</h2>
  <ul>
    <li>Enjoy a beautiful beach ride</li>
    <li>Easy to arrange private or group rides</li>
    <li>Professional guides and well trained horses</li>
    <li>No experience necessary</li>
  </ul>
</section>
<section class="abs card company">
  <h2>Company<br>Description</h2>
  <p>In 2004 Marcus Hale, an avid horseman, and his wife Dana, founded the company Saddle Coast Rides. Its true beginnings however were born decades earlier in Marcus's mind. His passion for horses began a child, when he learned how to care for the magnificent, graceful creatures.</p>
  <a class="read-more" href="#">Read More</a>
  <div class="organized">Organized By</div>
  <div class="badge" role="img" aria-label="Tour operator badge"></div>
  <a class="describes" href="#">Describes The Tour Operator</a>
</section>

<!-- Activity -->
<section class="activity">
  <h2 class="abs activity-title">Activity Description,</h2>
  <p class="abs activity-text">In 2004 Marcus Hale, an avid horseman, and his wife Dana, founded the company Saddle Coast Rides. Its true beginnings however were born decades earlier in Marcus's mind. His passion for horses began a child, when he learned how to care for the magnificent, graceful creatures.</p>
  <a class="abs read-more" href="#">Read More</a>
  <a class="abs chip" style="left:117px" href="#"><span class="ico"></span>Open Seasons<svg width="10" height="14" viewBox="0 0 10 14" fill="none" stroke="#fff" stroke-width="2"><path d="M2 1l6 6-6 6"/></svg></a>
  <a class="abs chip" style="left:273px" href="#"><span class="ico" style="border-radius:50%"></span>Languages Spoken<svg width="10" height="14" viewBox="0 0 10 14" fill="none" stroke="#fff" stroke-width="2"><path d="M2 1l6 6-6 6"/></svg></a>
  <a class="abs chip" style="left:428px" href="#"><span class="ico"></span>Cancellation Policy<svg width="10" height="14" viewBox="0 0 10 14" fill="none" stroke="#fff" stroke-width="2"><path d="M2 1l6 6-6 6"/></svg></a>
  <div class="fill" style="left:624px;top:1073px;width:576px;height:436px;background:linear-gradient(180deg,#8fb3a7 0%,#5f9a8c 40%,#3f7d73 100%)" role="img" aria-label="Photo of a rider swimming beside her horse in turquoise sea water"></div>
</section>

<!-- Booking band -->
<section>
  <div class="abs band" role="img" aria-label="Photo of a group of riders on horseback along a sandy beach"></div>
  <div class="abs price-card">
    <div class="price-top"><small>Starting From</small><strong>0,00,0000</strong></div>
    <div class="price-mid">
      <svg width="172" height="30" viewBox="0 0 172 30" fill="var(--green)">
        <g id="star"><path d="M15 1l4.1 8.6 9.4 1.2-6.9 6.5 1.8 9.3L15 22l-8.4 4.6 1.8-9.3L1.5 10.8l9.4-1.2z"/></g>
        <use href="#star" x="36"/><use href="#star" x="72"/><use href="#star" x="108"/><use href="#star" x="144"/>
      </svg>
      <a class="reviews" href="#">40 Reviews</a>
      <a class="btn-book" href="#">Book Now</a>
    </div>
    <div class="contact-row">
      <a href="#"><svg width="16" height="16" viewBox="0 0 16 16" fill="#555"><path d="M3.5 1l3 3-1.8 2.2c.9 1.9 2.3 3.3 4.1 4.1L11 8.5l3 3-1.8 2.5C7 14 2 9 1 3.3z"/></svg>Call Us</a>
      <a href="#"><svg width="20" height="14" viewBox="0 0 20 14" fill="none" stroke="#555" stroke-width="1.4"><rect x="1" y="1" width="18" height="12"/><path d="M1 1l9 7 9-7"/></svg>Email Us</a>
    </div>
  </div>
</section>

<!-- Tours -->
<section>
  <h2 class="abs section-title" style="top:2240px">Tours</h2>
  <div class="abs tour" style="top:2350px">
    <div class="icon-box"><svg width="64" height="64" viewBox="0 0 64 64" fill="none" stroke="#999" stroke-width="2"><circle cx="32" cy="32" r="26"/></svg></div>
    <h3>Group Tour</h3>
    <div class="price"><b>$75 USD</b> per person</div>
    <a class="btn btn-primary" href="#">Book Now<svg width="8" height="12" viewBox="0 0 8 12" fill="none" stroke="#fff" stroke-width="2"><path d="M1.5 1l5 5-5 5"/></svg></a>
    <a class="btn btn-outline" href="#">Add to Itinerary<svg width="8" height="12" viewBox="0 0 8 12" fill="none" stroke="#fff" stroke-width="2"><path d="M1.5 1l5 5-5 5"/></svg></a>
  </div>
  <a class="abs read-more tour-more" style="top:2515px" href="#">Read More</a>
  <div class="abs tour" style="top:2566px">
    <div class="icon-box"><svg width="64" height="64" viewBox="0 0 64 64" fill="none" stroke="#999" stroke-width="2"><circle cx="32" cy="32" r="26"/></svg></div>
    <h3>Private Tour</h3>
    <div class="price"><b>$90 USD</b> per person</div>
    <a class="btn btn-primary" href="#">Book Now<svg width="8" height="12" viewBox="0 0 8 12" fill="none" stroke="#fff" stroke-width="2"><path d="M1.5 1l5 5-5 5"/></svg></a>
    <a class="btn btn-outline" href="#">Add to Itinerary<svg width="8" height="12" viewBox="0 0 8 12" fill="none" stroke="#fff" stroke-width="2"><path d="M1.5 1l5 5-5 5"/></svg></a>
  </div>
  <a class="abs read-more tour-more" style="top:2734px" href="#">Read More</a>
</section>

<!-- Meeting point -->
<section class="meeting">
  <div class="abs map" role="img" aria-label="Street map around the meeting point on the West Bay coast"></div>
  <div class="abs meeting-bg"></div>
  <h2 class="abs meeting-title">Meeting Point</h2>
  <p class="abs meeting-addr">Lagoon Terrace Restaurant, 118 Harbour Reef Rd, West Bay, Cayman Islands</p>
  <a class="abs read-more" href="#">Get Direction</a>
</section>

<!-- Gallery -->
<section>
  <h2 class="abs section-title" style="top:3266px;font-size:40px">Photo Gallery</h2>
  <div class="photo" style="left:115px;top:3384px;width:485px;height:566px;background:linear-gradient(180deg,#7fb9c6 0%,#4ea3b4 35%,#c9c2b4 70%,#ddd6c8 100%)" role="img" aria-label="Photo of a woman riding a horse at the water's edge"></div>
  <div class="photo" style="left:614px;top:3384px;width:471px;height:277px;background:linear-gradient(180deg,#5a8fc7 0%,#53b3c0 40%,#d2c7b2 80%)" role="img" aria-label="Photo of a line of riders heading out of the sea"></div>
  <div class="photo" style="left:614px;top:3675px;width:471px;height:275px;background:linear-gradient(160deg,#2f6fae 0%,#3aa1c2 50%,#8fd0dc 100%)" role="img" aria-label="Photo of a horse splashing through the surf with a swimmer"></div>
</section>

<!-- Steps & recommended -->
<section>
  <div class="step-art" style="left:115px;top:4122px" role="img" aria-label="Illustration of a relaxed traveller choosing activities"></div>
  <div class="step-num" style="left:152px;top:4124px">1</div>
  <h3 class="step-title blue" style="left:115px;top:4340px">Choose Your<br>Favorite Activities</h3>
  <a class="abs read-more" style="left:115px;top:4408px" href="#">Read More</a>

  <div class="step-art" style="left:404px;top:4122px" role="img" aria-label="Illustration of a traveller planning online"></div>
  <div class="step-num" style="left:441px;top:4124px">2</div>
  <h3 class="step-title" style="left:404px;top:4340px">Use Our online<br>Travel partner</h3>
  <a class="abs read-more" style="left:404px;top:4408px" href="#">Read More</a>

  <div class="step-art" style="left:115px;top:4480px" role="img" aria-label="Illustration of travel arrangements being made"></div>
  <div class="step-num" style="left:152px;top:4490px">3</div>
  <h3 class="step-title" style="left:115px;top:4698px">We make All The<br>Arrangements</h3>
  <a class="abs read-more" style="left:115px;top:4764px" href="#">Read More</a>

  <div class="step-art" style="left:404px;top:4480px" role="img" aria-label="Illustration of travellers relaxing on the beach"></div>
  <div class="step-num" style="left:441px;top:4490px">4</div>
  <h3 class="step-title" style="left:404px;top:4698px">Relax and Enjoy<br>Your Vacation</h3>
  <a class="abs read-more" style="left:404px;top:4764px" href="#">Read More</a>

  <div class="abs recommended" role="img" aria-label="Photo of a rider on horseback silhouetted against the sunset">
    <h2>Recommended<br>Activities</h2>
  </div>
</section>

<!-- Footer -->
<footer>
  <div class="abs footer">
    <a class="brand" href="#"><span class="mark"></span>TideRoute</a>
    <nav class="footnav">
      <a class="active" href="#">Discover Cayman</a>
      <a href="#">Things To do</a>
      <a href="#">My Trip Planner</a>
      <a href="#">Map</a>
      <a href="#">Contact Us</a>
    </nav>
  </div>
  <div class="abs copyright">Copyright © 2019 TideRoute. All rights reserved.</div>
</footer>

</body>
</html>
```